Qorvant Flyer Design Project

We need a new flyer design for our company based in Australia. We provide Business Valuations for small businesses. The flyer should follow the same colours and theme as our website www.qorvant.com.au and our logo. The design should communicate a professional financial services company. It should be a simple design (not too 'busy') and have a sleek and professional feel to it. It will be used to send to prospective clients and referral sources to tell about our company and prompt them to call us or visit our website.

Target Market(s)

Business owners and people working in financial services (accountants, financial planners etc)

Industry/Entity Type

Financial

Requirements
Must have
• Must be DL double sided, (99mm x 210mm) and use CMYK colours. Must contain trim marks for printer and be print ready.

```html
<!DOCTYPE html>
<html lang="en">
<head>
<meta charset="utf-8">
<title>Qorvant – Business Valuations DL Flyer</title>
<link rel="stylesheet" href="https://fonts.googleapis.com/css2?family=Alfa+Slab+One&family=Source+Sans+3:wght@400;600;700&display=swap">
<style>
  :root{
    --navy:#2b3990;
    --navy-deep:#1f2a78;
    --lime:#8dc63f;
    --lime-dark:#6fa82a;
    --ink:#2a2a35;
    --paper:#ffffff;
    --canvas:#ffffff;
    --photo-light:#c9d7e6;
    --photo-dark:#5d7896;
  }
  *{box-sizing:border-box;margin:0;padding:0}
  html,body{width:1144px;height:1200px;overflow:hidden;background:var(--canvas)}
  body{position:relative;font-family:"Source Sans 3",Arial,sans-serif;color:var(--ink)}

  .panel{position:absolute;top:25px;width:516px;height:1125px;overflow:hidden;background:var(--paper);
    box-shadow:4px 5px 8px rgba(0,0,0,.25)}
  .panel--front{left:42px}
  .panel--back{left:586px;border:1px solid #ddd}
  .panel__bg{position:absolute;inset:0;width:100%;height:100%}

  /* front */
  .brand-name{position:absolute;left:0;width:100%;top:296px;text-align:center;
    font-weight:700;font-size:84px;line-height:1;color:var(--navy);letter-spacing:-1px}
  .front-title{position:absolute;left:0;width:100%;top:420px;text-align:center;
    font-family:"Alfa Slab One",Georgia,serif;font-weight:400;font-size:62px;line-height:1.1;color:#fff;
    text-shadow:3px 3px 4px rgba(0,0,0,.45)}
  .photo{position:absolute;left:-60px;top:565px}
  .price-tab{position:absolute;right:0;top:705px;width:170px;height:160px;background:var(--navy);
    border-radius:80px 0 0 80px;border:4px solid #fff;border-right:none;color:#fff;text-align:right;padding:16px 14px 0 0}
  .price-tab__label{font-weight:700;font-size:40px;line-height:1}
  .price-tab__amount{font-weight:700;font-size:30px;margin-top:6px}
  .price-tab__amount small{font-weight:400;font-size:21px}
  .tagline{position:absolute;left:0;width:100%;top:995px;height:52px;background:var(--navy);color:#fff;
    text-align:center;font-weight:700;font-size:27px;line-height:52px}

  /* back */
  .why{position:absolute;left:40px;top:82px;font-weight:400;line-height:1}
  .why__line{display:block;font-family:"Alfa Slab One",Georgia,serif;font-size:60px;color:var(--lime);line-height:1}
  .why__brand{display:block;font-weight:700;font-size:64px;color:var(--navy);letter-spacing:-1px;line-height:1.05}
  .why__mark{color:var(--lime)}
  .benefits{position:absolute;left:36px;top:316px;width:400px;list-style:none}
  .benefits li{position:relative;padding-left:48px;font-size:17px;line-height:1.2;margin-bottom:15px}
  .benefits li::before{content:"";position:absolute;left:0;top:-1px;width:24px;height:24px;border-radius:50%;
    background:radial-gradient(circle at 35% 30%,#7d8fe0 0,var(--navy) 55%,var(--navy-deep) 100%)}
  .benefits strong{color:var(--navy);font-weight:700}
  .cta-box{position:absolute;left:80px;top:800px;width:396px;height:58px;background:var(--navy);border-radius:10px;
    color:#fff;font-weight:700;font-size:19.5px;line-height:1.2;text-align:left;padding:6px 0 0 34px}
  .contact{position:absolute;left:40px;top:884px;display:flex;align-items:flex-start;gap:26px}
  .contact__name{font-weight:700;font-size:64px;line-height:1;color:var(--navy);letter-spacing:-1px;margin-top:8px}
  .contact__list{list-style:none;font-size:16.5px;line-height:1.22;color:var(--ink)}
  .contact__list b{color:var(--lime);font-weight:700}
  .contact__list .web{font-weight:700;color:var(--navy)}
</style>
</head>
<body>

<section class="panel panel--front" aria-label="Flyer front">
  <svg class="panel__bg" viewBox="0 0 516 1125" preserveAspectRatio="none" aria-hidden="true">
    <rect width="516" height="1125" fill="var(--navy)"/>
    <path d="M516 0 L516 70 C320 95 120 190 0 330 L0 300 C110 150 300 40 470 0 Z" fill="#fff"/>
    <path d="M516 70 C320 95 120 190 0 330 L0 995 L516 995 Z" fill="var(--lime)"/>
    <rect y="1047" width="516" height="78" fill="#fff"/>
  </svg>
  <div class="brand-name">qorvant</div>
  <h1 class="front-title">Business<br>Valuations</h1>
  <svg class="photo" width="500" height="440" viewBox="0 0 500 440">
    <defs>
      <linearGradient id="photoTone" x1="0" y1="0" x2="1" y2="1">
        <stop offset="0" stop-color="var(--photo-light)"/>
        <stop offset="1" stop-color="var(--photo-dark)"/>
      </linearGradient>
    </defs>
    <circle cx="248" cy="248" r="246" fill="#fff"/>
    <circle cx="248" cy="248" r="236" fill="url(#photoTone)" role="img" aria-label="Photo of a fountain pen resting on financial charts"/>
  </svg>
  <div class="price-tab">
    <div class="price-tab__label">Fixed<br>Price</div>
    <div class="price-tab__amount">$540 <small>(+gst)</small></div>
  </div>
  <div class="tagline">Business valuation specialists</div>
</section>

<section class="panel panel--back" aria-label="Flyer back">
  <svg class="panel__bg" viewBox="0 0 516 1125" preserveAspectRatio="none" aria-hidden="true">
    <path d="M516 0 L516 330 C480 220 410 110 300 0 Z" fill="var(--lime)"/>
    <path d="M516 0 L516 250 C480 160 430 70 370 0 Z" fill="var(--navy)"/>
    <path d="M0 1005 C130 1070 330 1085 516 1072 L516 1125 L0 1125 Z" fill="var(--lime)"/>
    <path d="M0 1075 C160 1105 340 1110 516 1100 L516 1125 L0 1125 Z" fill="var(--navy)"/>
  </svg>
  <h2 class="why">
    <span class="why__line">Why</span>
    <span class="why__line">Use</span>
    <span class="why__brand">qorvant <span class="why__mark">?</span></span>
  </h2>
  <ul class="benefits">
    <li><strong>All reports are prepared by a qualified Accountant</strong></li>
    <li><strong>Specialised</strong> – valuing small to medium businesses is all we do</li>
    <li>We use our experience to compare and benchmark similar businesses across Australia</li>
    <li>A valuation appraisal report emailed to you with our comments and valuation estimate</li>
    <li><strong>Five business day turnaround!</strong></li>
    <li>A follow up phone call from an Accountant to discuss the valuation and answer any questions you have</li>
    <li><strong>Fixed price of only $540 (+gst)</strong></li>
    <li>Our clients include Business Buyers and Sellers, Accountants, Solicitors, Financial Planners, Franchisors and Franchisees</li>
  </ul>
  <div class="cta-box">For more info call 1300 555 014<br>or visit www.qorvant.com.au</div>
  <div class="contact">
    <div class="contact__name">qorvant</div>
    <ul class="contact__list">
      <li><b>T.</b> 1300 555 014</li>
      <li><b>F.</b> 07 5550 1287</li>
      <li><b>E.</b> info@qorvant.com.au</li>
      <li class="web">www.qorvant.com.au</li>
      <li>ABN – 41 902 318 775</li>
    </ul>
  </div>
</section>

</body>
</html>
```